Making 6 Posters and 2 large posters for coffee shop

We are Brindle Mug Depot (similar to a brewhollow), planning to make 3 boards for menu, 3 photos to be printed onto the board, and 2 large posters. (dimensions provided). We believe this is a very simple project with not much additional work required as all pictures have been provided.
We are asking for minimalist design. Very simple. All photos have been provided. 3 of the boards, and 2 for the large posters. The menu has been done but it is in PDF and require recreation (pls make similar design)
The menu board and the 3 other photos are roughly square shape. While dimensions are not provided by our contractors yet, designers can roughly get the dimension from the photos of the boards we are planning to replace.
All these posters will be printed with no frames. So it will look something like those menu board at brewhollow.
Urgently need it in next 24 hours.
Instructions all in PPT attached.
File Link provided:
http://qlinkbox.example/7hT3kWz
Thanks.
---- Edited
For the pictures, we are looking for borders like this if possible (VORN - expensive looking border but platinum white, and dark background.) for the large poster, we liek black themed background with some glow if possible around the cups like the kelvaro logo)
http://www.plumtemplates.example/images/thumbs/Onyx-Slate-psd48213.png
http://www.wirefable-news.example/wp-content/uploads/2013/11/kelvaro-signage.jpg
Target Market(s)
Professionals - Lawyers, Bankers, Brokers
Industry/Entity Type
Coffee Shop

```html
<!DOCTYPE html>
<html lang="en">
<head>
<meta charset="utf-8">
<title>Brindle Mug Depot — Menu Boards</title>
<link rel="stylesheet" href="https://fonts.googleapis.com/css2?family=Oswald:wght@500;700&family=Roboto+Condensed:wght@400;700&display=swap">
<style>
  :root {
    --page: #f2f2f0;
    --board: #0c0c0c;
    --platinum: #dcd9d2;
    --inner-line: #6a6a6a;
    --text: #f4f4f4;
    --muted: #b9b9b9;
    --accent: #e8c21a;
  }
  * { box-sizing: border-box; margin: 0; padding: 0; }
  html, body {
    width: 1200px; height: 900px; overflow: hidden;
    background: var(--page);
  }
  .board-row {
    position: absolute; left: 21px; top: 358px;
    display: flex; gap: 11px;
  }
  .board {
    position: relative;
    width: 184px; height: 184px;
    background: var(--board);
    border: 3px solid var(--platinum);
    color: var(--text);
    font-family: "Roboto Condensed", sans-serif;
  }
  .board::after {
    content: ""; position: absolute; inset: 4px;
    border: 1px solid var(--inner-line); pointer-events: none;
  }
  /* photo boards */
  .brand-tag {
    position: absolute; left: 12px; top: 12px;
    display: flex; align-items: center; gap: 4px;
    font-size: 5px; font-weight: 700; letter-spacing: .3px;
    text-transform: uppercase; color: var(--text);
  }
  .brand-dot { width: 9px; height: 9px; border-radius: 50%; background: var(--accent); }
  .photo { position: absolute; }
  .photo--coffee {
    left: 18px; top: 58px; width: 140px; height: 80px;
    background: radial-gradient(ellipse at 60% 55%, #e2c23a 0 30%, #8a6a2a 45%, #3a2414 62%, transparent 75%);
  }
  .photo--sandwich {
    left: 28px; top: 70px; width: 130px; height: 70px;
    background: radial-gradient(ellipse at 50% 50%, #b8772e 0 32%, #c9c23a 48%, #a8a22a 62%, transparent 72%);
  }
  .photo--waffle {
    left: 38px; top: 50px; width: 110px; height: 110px;
    background: radial-gradient(circle at 50% 50%, #f0ece0 0 16%, #b06a2e 30%, #8a4a20 50%, #c99e4a 62%, transparent 70%);
  }
  /* menu boards */
  .menu { padding: 12px 14px; }
  .menu-title {
    font-family: "Oswald", sans-serif; font-weight: 700;
    font-size: 10px; letter-spacing: 1px; text-align: center;
    text-transform: uppercase; margin-bottom: 4px;
  }
  .menu-title--sub { margin-top: 10px; }
  .menu-rule { height: 1px; background: var(--inner-line); margin: 3px 0 5px; }
  .price-list { list-style: none; font-size: 5.5px; }
  .price-list li {
    display: grid; grid-template-columns: 1fr 16px 16px;
    padding: 2.2px 0; border-bottom: 1px solid #2a2a2a;
  }
  .price-list li span:not(:first-child) { text-align: right; color: var(--muted); }
  .price-list .col-head { color: var(--muted); font-weight: 700; }
  .price-list--single li { grid-template-columns: 1fr 18px; }
  .menu--food { padding-top: 8px; }
</style>
</head>
<body>
<main class="board-row">
  <section class="board board--photo">
    <div class="brand-tag"><span class="brand-dot"></span>Brindle Mug Depot</div>
    <div class="photo photo--coffee" role="img" aria-label="Latte in a yellow cup and saucer with scattered coffee beans"></div>
  </section>

  <section class="board menu">
    <h2 class="menu-title">Hot Beverage</h2>
    <div class="menu-rule"></div>
    <ul class="price-list">
      <li class="col-head"><span></span><span>Reg</span><span>Lg</span></li>
      <li><span>Espresso</span><span>2.80</span><span>3.20</span></li>
      <li><span>Americano</span><span>3.00</span><span>3.50</span></li>
      <li><span>Cappuccino</span><span>3.60</span><span>4.20</span></li>
      <li><span>Caffe Latte</span><span>3.60</span><span>4.20</span></li>
      <li><span>Flat White</span><span>3.80</span><span>4.40</span></li>
      <li><span>Mocha</span><span>4.00</span><span>4.60</span></li>
      <li><span>Hot Chocolate</span><span>3.40</span><span>3.90</span></li>
      <li><span>Chai Latte</span><span>3.80</span><span>4.30</span></li>
    </ul>
  </section>

  <section class="board board--photo">
    <div class="brand-tag"><span class="brand-dot"></span>Brindle Mug Depot</div>
    <div class="photo photo--sandwich" role="img" aria-label="Croissant sandwich on a yellow plate"></div>
  </section>

  <section class="board menu">
    <h2 class="menu-title">Iced Beverage</h2>
    <div class="menu-rule"></div>
    <ul class="price-list">
      <li class="col-head"><span></span><span>Reg</span><span>Lg</span></li>
      <li><span>Iced Latte</span><span>3.90</span><span>4.50</span></li>
      <li><span>Iced Mocha</span><span>4.20</span><span>4.80</span></li>
      <li><span>Cold Brew</span><span>3.80</span><span>4.40</span></li>
      <li><span>Iced Americano</span><span>3.20</span><span>3.70</span></li>
      <li><span>Iced Tea</span><span>2.90</span><span>3.40</span></li>
      <li><span>Lemonade</span><span>2.90</span><span>3.40</span></li>
    </ul>
  </section>

  <section class="board board--photo">
    <div class="brand-tag"><span class="brand-dot"></span>Brindle Mug Depot</div>
    <div class="photo photo--waffle" role="img" aria-label="Waffle topped with ice cream on a round plate"></div>
  </section>

  <section class="board menu menu--food">
    <h2 class="menu-title">Waffles</h2>
    <ul class="price-list price-list--single">
      <li><span>Classic Waffle</span><span>5.50</span></li>
      <li><span>Berry Waffle</span><span>6.50</span></li>
    </ul>
    <h2 class="menu-title menu-title--sub">Salad</h2>
    <ul class="price-list price-list--single">
      <li><span>Garden Salad</span><span>6.90</span></li>
      <li><span>Chicken Salad</span><span>7.90</span></li>
    </ul>
    <h2 class="menu-title menu-title--sub">Sandwiches</h2>
    <ul class="price-list price-list--single">
      <li><span>Club Sandwich</span><span>7.50</span></li>
      <li><span>Tuna Melt</span><span>6.90</span></li>
    </ul>
  </section>
</main>
</body>
</html>
```